Harborview Tap & Grille Menu Makeover

I am looking for a professional look to update our current menu. We are an independently owned sports bar and grill. Up to this point, I have done all of my own graphic designing. I am looking for something classy/family oriented. We are a very family friendly sports bar that offers a wide variety of menu options. Our website is www.harborviewtapgrille.example. This may help you get more of a feel for what type of place we are and what we offer. Our menu is listed on the website. My current menu is 8.5x14 inserts that feature a cover page, 4 inside pages and a back page. I would like something a little more condensed than this. Possibly a large tri-fold menu? I am open to all new ideas. I do have some pictures on my menu now, and would like to continue using a few pictures to feature some of my items. I would like something that is in a format that gives me the option to change items and prices on my own in the future. I would also like it to feature, or inform my patrons about our technology that we offer. We offer online ordering and we are a "verified venue" with Brewlogr.( a social site for craft beer lovers).

Industry/Entity Type

Sports Bar

Requirements
Nice to have
• Nice to have some pictures, but does not have to. We do feature 9 different beers on tap. A lot of them are local craft beers from the state of Kansas. Not sure if that is something we can feature, but it is a nice talking point. All of our tables and bar are hand built. With a rich mahogany finish on all of our woodwork, some type of "woodgrain" look into the menu would be nice.

```html
<!DOCTYPE html>
<html lang="en">
<head>
<meta charset="utf-8">
<title>Harborview Tap &amp; Grille — Menu</title>
<link href="https://fonts.googleapis.com/css2?family=Cinzel:wght@600;700&family=Playfair+Display:wght@500&family=Oswald:wght@300;400&family=Montserrat:wght@700&display=swap" rel="stylesheet">
<style>
:root{
  --wood-dark:#5a1f0c;
  --wood-mid:#8a3a17;
  --wood-light:#a8501f;
  --paper:#dcc7a2;
  --paper-edge:#a98356;
  --ink:#1c140d;
  --ink-soft:#3a2a1c;
}
*{margin:0;padding:0;box-sizing:border-box}
html,body{width:850px;height:1200px;overflow:hidden}
body{
  position:relative;
  background:
    repeating-linear-gradient(90deg,rgba(0,0,0,.08) 0 2px,transparent 2px 140px),
    linear-gradient(90deg,var(--wood-dark),var(--wood-mid) 25%,var(--wood-light) 50%,var(--wood-mid) 75%,var(--wood-dark));
  color:var(--ink);
}
.masthead{position:absolute;top:40px;left:0;width:850px;text-align:center}
.rule{position:absolute;height:2px;background:var(--ink)}
.rule::before,.rule::after{content:"";position:absolute;top:-2px;width:6px;height:6px;border-radius:50%;background:var(--ink)}
.rule::before{left:-3px}.rule::after{right:-3px}
.rule-top{top:19px;left:218px;width:416px}
.rule-bottom{top:127px;left:294px;width:268px}
.brand{position:absolute;top:28px;width:100%;font-family:"Cinzel",serif;font-weight:700;font-size:44px;letter-spacing:8px;line-height:1}
.brand-sub{position:absolute;top:88px;width:100%;font-family:"Cinzel",serif;font-weight:700;font-size:20px;letter-spacing:1px}
.paper{position:absolute;left:0;top:0}
.photo{position:absolute;border-radius:50%}
.photo-eggrolls{left:608px;top:260px;width:152px;height:152px;background:radial-gradient(circle at 50% 45%,#f1ecd8 0 14%,#d4a93c 30%,#6f8a2e 60%,#14140f 78%)}
.photo-berries{left:646px;top:694px;width:104px;height:104px;background:radial-gradient(circle at 50% 50%,#2a1d2e 0 20%,#c23a2c 45%,#e2b63a 65%,#3f6a2a 90%)}
.section-title{position:absolute;left:94px;font-family:"Playfair Display",serif;font-weight:500;font-size:38px;letter-spacing:-.5px}
.item{position:absolute;width:330px}
.item.left{left:98px}
.item.right{left:427px;width:330px}
.item h3{font-family:"Oswald",sans-serif;font-weight:400;font-size:15px;line-height:17px;text-transform:uppercase;letter-spacing:-.2px}
.item p{font-family:"Oswald",sans-serif;font-weight:300;font-size:8.6px;line-height:12px;text-transform:uppercase;color:var(--ink-soft)}
.price{font-family:"Montserrat",sans-serif;font-weight:700;font-size:7.4px;letter-spacing:.4px;line-height:9px}
.divider{position:absolute;top:733px;left:200px;width:440px;height:1px;background:var(--ink)}
.divider-mark{position:absolute;left:214px;top:-4px;width:12px;height:9px;border:2px solid var(--ink);border-radius:50%;background:var(--paper)}
</style>
</head>
<body>
<header class="masthead">
  <div class="rule rule-top"></div>
  <h1 class="brand">HARBORVIEW</h1>
  <div class="brand-sub">TAP &amp; GRILLE</div>
  <div class="rule rule-bottom"></div>
</header>

<svg class="paper" width="850" height="1200" viewBox="0 0 850 1200" aria-hidden="true">
  <defs>
    <radialGradient id="parch" cx="50%" cy="50%" r="70%">
      <stop offset="0" stop-color="#e2cfac"/>
      <stop offset=".7" stop-color="#d3ba91"/>
      <stop offset="1" stop-color="#a98356"/>
    </radialGradient>
  </defs>
  <path fill="url(#parch)" d="M66 222 L120 214 L150 222 L210 212 L300 219 L360 210 L420 218 L470 209 L520 220 L600 212 L660 221 L720 210 L762 222 L790 216 L800 250 L790 300 L800 360 L792 420 L802 500 L794 560 L800 620 L788 680 L798 740 L790 800 L800 880 L792 940 L802 1010 L790 1080 L798 1130 L760 1148 L700 1140 L640 1150 L560 1142 L480 1152 L400 1143 L330 1151 L260 1141 L190 1150 L120 1142 L70 1150 L56 1110 L64 1060 L52 1000 L62 940 L50 880 L60 820 L48 760 L60 700 L50 640 L58 580 L46 520 L58 460 L50 400 L60 340 L48 280 Z"/>
</svg>

<div class="photo photo-eggrolls" role="img" aria-label="Photo of southwest chicken eggrolls with ranch dipping sauce"></div>
<div class="photo photo-berries" role="img" aria-label="Photo of summer berry salad with fresh berries on spinach"></div>

<h2 class="section-title" style="top:300px">APPETIZERS</h2>

<div class="item left" style="top:350px"><h3>Slider Burgers</h3><p>Six juicy bite sized burgers topped with American cheese and served with pickle slices.</p><div class="price">8.99</div></div>
<div class="item left" style="top:406px"><h3>Loaded Potato Skins</h3><p>Six crispy skins loaded with jack, cheddar and mozzarella cheese, then topped with smoked bacon and green onions. Served with sour cream.</p><div class="price">8.99</div></div>
<div class="item left" style="top:462px"><h3>Rattlesnake Eggs</h3><p>A spicy combo of pepper jack cheese and jalapeños, battered and fried.</p><div class="price">7.99</div></div>
<div class="item left" style="top:506px"><h3>Mozzarella Cheese Sticks</h3><p>Classic battered mozzarella cheese sticks served with ranch dressing.</p><div class="price">7.99</div></div>
<div class="item left" style="top:550px"><h3>Grand Slam French Fries</h3><p>French fries loaded with jack, cheddar, mozzarella, bacon, jalapeños and green onions! Served with ranch dressing.</p><div class="price">7.99</div></div>
<div class="item left" style="top:606px"><h3>Bang Bang Shrimp</h3><p>Lightly breaded and fried shrimp coated with a spicy Thai sauce, topped with parmesan cheese and diced tomatoes. Served over a bed of romaine lettuce.</p><div class="price">7.99</div></div>
<div class="item left" style="top:662px"><h3>Ballpark Pretzel Basket</h3><p>Buttered and salted pretzels served with nacho cheese sauce.</p><div class="price">7.99</div></div>

<div class="item right" style="top:350px"><h3>Spicy Southwest Chicken Eggrolls</h3><p>Stuffed with black beans, corn and chicken. Served with southwest ranch.</p><div class="price">9.99</div></div>
<div class="item right" style="top:394px"><h3>Blooming Onion</h3><p>This fan favorite is classically carved and deep fried to perfection. Served with Harborview signature dipping sauce.</p><div class="price">7.99</div></div>
<div class="item right" style="top:450px"><h3>Chicken Quesadilla</h3><p>A 12 inch flour tortilla stuffed with grilled chicken and jack and cheddar cheese. Served with salsa.</p><div class="price">8.99</div></div>
<div class="item right" style="top:506px"><h3>Marlow's Boneless Buffalo Wings</h3><p>A full pound of spicy, boneless buffalo wings. Served with ranch dressing or Marlow's Gold Label sauce.</p><div class="price">7.99</div></div>
<div class="item right" style="top:562px"><h3>Harborview Loaded Nachos</h3><p>Tri-colored tortilla chips smothered with creamy Monterey jack cheese, choice of beef or chicken, and topped with grilled peppers and onions, jalapeños and diced tomatoes. Served with sour cream and salsa.</p><div class="price">9.99</div></div>
<div class="item right" style="top:630px"><h3>Garlic Bread Basket</h3><p>Tri-colored tortilla chips smothered with creamy Monterey jack cheese, choice of beef or chicken, and topped with grilled peppers and onions, jalapeños and diced tomatoes. Served with sour cream and salsa.</p><div class="price">9.99</div></div>

<div class="divider"><span class="divider-mark"></span></div>

<h2 class="section-title" style="top:755px">SALADS</h2>

<div class="item left" style="top:807px"><h3>Chicken Tender Garden Salad</h3><p>A spring lettuce mix topped with shredded jack and cheddar cheese, garden vegetables, bacon, croutons and egg. With your choice of crispy or grilled chicken.</p><div class="price">LARGE 8.99 / SMALL 7.99</div></div>
<div class="item left" style="top:863px"><h3>Nacho Crunchito Salad</h3><p>Harborview's unique blend of iceberg lettuce, topped with jack and cheddar cheese, tomatoes, black olives, ranch style beans and creamy Italian dressing. Topped with Crunchito chips</p><div class="price">LARGE 8.99 / SMALL 7.99</div></div>
<div class="item left" style="top:931px"><h3>Cobb Salad</h3><p>Rows of ham, turkey and roast beef, side by side with baby corn, jack and cheddar cheese, egg slices, garden vegetables, bacon and croutons served over iceberg lettuce.</p><div class="price">LARGE 8.99 / SMALL 7.99</div></div>
<div class="item left" style="top:999px"><h3>Summer Berry Salad</h3><p>A blend of fresh berries, tomatoes, croutons, mandarin oranges and crumbled feta cheese served on fresh spinach leaves. Your choice of chicken or shrimp.</p><div class="price">LARGE 8.99 / SMALL 7.99</div></div>

<div class="item right" style="top:807px"><h3>House Caesar Salad</h3><p>A classic mix of crisp romaine lettuce, shredded parmesan cheese, and croutons. Served with our signature Caesar dressing.</p><div class="price">LARGE 6.99 / SMALL 5.99<br>LARGE WITH CHICKEN 8.99 / SMALL WITH CHICKEN 6.99</div></div>
<div class="item right" style="top:871px"><h3>Nacho Crunchito Salad</h3><p>Harborview's unique blend of iceberg lettuce, topped with jack and cheddar cheese, tomatoes, black olives, ranch style beans and creamy Italian dressing. Topped with Crunchito chips.</p><div class="price">LARGE 8.99 / SMALL 7.99</div></div>
<div class="item right" style="top:939px"><h3>Cobb Salad</h3><p>Rows of ham, turkey and roast beef, side by side with baby corn, jack and cheddar cheese, egg slices, garden vegetables, bacon and croutons served over iceberg lettuce.</p><div class="price">LARGE 8.99 / SMALL 7.99</div></div>
<div class="item right" style="top:1007px"><h3>Summer Berry Salad</h3><p>A blend of fresh berries, tomatoes, croutons, mandarin oranges and crumbled feta cheese served on fresh spinach leaves. Your choice of chicken or shrimp.</p><div class="price">LARGE 8.99 / SMALL 7.99</div></div>
</body>
</html>
```